Web Design for Webdesign company 3 page PSD

Project
---------
We need a PSD Web Design to be used in a WordPress installation.
What we would like to create is a professional looking website for a web design agency. We also need you to look for suitable stock images to be placed on these pages.
We need the design for:
Homepage
Landing page
Contact page
attached in the pages file you will find a file with more in depth details how these files should be build up.
We would like to see a desktop version and a mobile version of these pages
The website should have a 1100px width.
The mobile design should have 480px width.
The homepage should have a header slider about 450px high.
The slider is preferred full width and should have some images text and a button
Objectives
-------------
The main objective for the website is to get leads from customers in the form of a request for a quotation or a call or mail me back action. The most important action for the homepage is to link and navigate to our landing pages.
What we want to tell our visitors (our main products)
-------------------------------------------------------------------
- A website with no big investment but a monthly rate
- A successful website with no worries (a complete website, seo, hosting and a service contract for future customization is included for a monthly rate)
Color Scheme
------------
Use branding colors. You can find them in the branding.pdf file.
Additional colors:
White: #ffffff
Black: #181818
Company info
--------------
We are a starting web design / marketing agency based in The Netherlands and looking for the design of our website. Our services are (custom) webdesign, website marketing or combinations of both. Our main customer group is small business owners.
We sell websites but give the option to buy it with a lease contract.
A second product is a default website with a complete service: SEO, hosting and a service contract for a monthly rate.
Content:
-----------
If not available place Lorem Ipsum text.
There will come about 400 words of text on the landing pages
Design Competition
--------------------------
Since this is a designing competition we would like to see your creativity.
What you can expect from us is a lot of feedback 7 days a week with short response time.
You can send us the first sketchy mock ups of the homepage and we will give feedback based on these design. But we like your feedback or comments as well
Read the pages file for more in depth details how the pages should be designed

Target Market(s)
Small business owners in The Netherlands
Industry/Entity Type
It Company
Number of Pages Required
3 page
Requirements
Must have
- Homepage:
- Header slider with images, some text and a link to a custom page
- The slider should have 3 designed slides
- Landings page:
- Sidebar
- Action button for a request for a quotation
- Action button for a call me back action
- Action button for an appointment
- Contact form:
- Address details
- Contact form
Nice to have
- Homepage:
- Full width slider
- Testimonial block
- Blog items
Should not have
- Flash
- A to crowded design

```html
<!DOCTYPE html>
<html lang="en">
<head>
<meta charset="utf-8">
<title>Birchline Web Studio – Home</title>
<link href="https://fonts.googleapis.com/css2?family=Open+Sans:wght@300;400;600&family=Ubuntu:wght@300;400;700&display=swap" rel="stylesheet">
<style>
:root{
  --teal:#2e8a86;
  --teal-dark:#2f7f76;
  --green:#6cbf7b;
  --hero-a:#27a985;
  --hero-b:#5fc47a;
  --wood:#b9a592;
  --ink:#181818;
  --text:#444;
  --muted:#777;
  --line:#e6e6e6;
  --footer:#f4f4f4;
  --bar:#262626;
  --white:#ffffff;
}
*{margin:0;padding:0;box-sizing:border-box}
html,body{width:898px;height:1200px;overflow:hidden;background:var(--white)}
body{position:relative;font-family:"Open Sans",sans-serif;color:var(--text)}
.abs{position:absolute}

/* header */
.site-header{left:0;top:0;width:898px;height:86px;background:var(--white);border-top:1px solid #ddd}
.brand{left:74px;top:30px;display:flex;align-items:center;gap:8px;font-family:"Open Sans",sans-serif;font-weight:600;font-size:17px;color:var(--teal);letter-spacing:.3px}
.brand-dot{width:14px;height:14px;border-radius:50%;background:var(--teal)}
.main-nav{top:39px;font-size:9.6px;color:#333;letter-spacing:.2px}
.nav-active{left:470px;top:0;width:43px;height:2px;background:var(--teal)}

/* hero */
.hero{left:0;top:86px;width:898px;height:393px;background:linear-gradient(160deg,var(--hero-a) 0%,#2fb083 55%,var(--hero-b) 100%)}
.hero-floor{left:0;top:423px;width:898px;height:56px;background:linear-gradient(180deg,#c6b3a0,var(--wood) 60%,#a99480)}
.hero-photo{left:88px;top:125px;width:278px;height:346px;border-radius:120px 120px 20px 20px;background:linear-gradient(180deg,rgba(210,140,110,.55),rgba(90,110,150,.55));}
.hero-title{left:400px;width:356px;text-align:center;font-family:"Ubuntu",sans-serif;color:var(--white)}
.hero-btn{left:502px;top:371px;width:159px;height:34px;background:var(--white);border-radius:2px;font-family:"Ubuntu",sans-serif;font-size:12px;color:var(--teal-dark);display:flex;align-items:center;justify-content:center;gap:5px;box-shadow:0 1px 3px rgba(0,0,0,.2)}
.slide-arrow{top:256px;width:26px;height:26px;border-radius:50%;background:#1e6e55;opacity:.85}

/* section titles */
.section-title{top:513px;font-weight:300;font-size:16px;color:#333}

/* blog */
.blog-card{width:239px;height:180px}
.blog-date{left:16px;top:125px;height:20px;display:flex;font-size:8.8px;font-weight:600;color:var(--white)}
.blog-date .ico{width:20px;background:var(--green);display:flex;align-items:center;justify-content:center}
.blog-date .lbl{background:var(--teal-dark);padding:0 9px;line-height:20px}
.blog-caption{left:16px;top:152px;font-size:11.2px;color:var(--white)}

/* testimonials */
.quote{left:630px;width:212px;font-size:8.6px;line-height:18px;color:#555}
.quote-mark{font-family:Georgia,serif;font-size:22px;color:#ccc;line-height:10px;vertical-align:-6px;margin-right:6px}
.avatar{width:58px;height:58px;border-radius:50%}
.person{left:700px;width:136px;font-size:9.6px;padding-bottom:8px;border-bottom:1px solid var(--line)}
.person .name{color:var(--teal)}
.pager{left:700px;display:flex;gap:4px}
.pager span{width:16px;height:16px;border:1px solid var(--line);font-size:10px;color:#c0392b;display:flex;align-items:center;justify-content:center}

/* footer */
.site-footer{left:0;top:982px;width:898px;height:174px;background:var(--footer);border-top:1px solid #e8e8e8}
.footer-title{top:1013px;font-size:11.4px;color:#333}
.footer-text{font-size:8.8px;line-height:15.5px;color:#444}
.social{top:1107px;width:22px;height:22px}
.news-input{left:421px;top:1075px;width:123px;height:31px;background:var(--white);border:1px solid #ddd;font-size:8.4px;color:#555;padding:0 10px;line-height:29px}
.news-btn{left:544px;top:1075px;width:73px;height:31px;background:var(--green);color:var(--white);font-size:9.4px;line-height:31px;text-align:center}
.contact-line{left:696px;font-size:9.8px;color:#333;display:flex;align-items:center;gap:10px}
.bottom-bar{left:0;top:1156px;width:898px;height:44px;background:var(--bar);text-align:center;line-height:44px;font-size:8.6px;color:#aaa}
.bottom-bar b{color:var(--green);font-weight:600}
</style>
</head>
<body>

<header class="abs site-header">
  <div class="abs nav-active"></div>
  <div class="abs brand"><span class="brand-dot"></span>BIRCHLINE WEB STUDIO</div>
  <nav>
    <span class="abs main-nav" style="left:477px">HOME</span>
    <span class="abs main-nav" style="left:538px">ABOUT US</span>
    <span class="abs main-nav" style="left:617px">OUR SERVICES</span>
    <span class="abs main-nav" style="left:712px">NEWS</span>
    <span class="abs main-nav" style="left:770px">CONTACT US</span>
  </nav>
</header>

<section class="abs hero"></section>
<div class="abs hero-floor" role="img" aria-label="Wooden floor boards"></div>
<div class="abs hero-photo" role="img" aria-label="Photo of a smiling woman sitting cross-legged with a laptop, giving a thumbs up"></div>
<div class="abs hero-title" style="top:246px;font-size:38px;font-weight:700">RESPONSIVE</div>
<div class="abs hero-title" style="top:289px;font-size:28px;font-weight:400">Web Design</div>
<div class="abs hero-title" style="top:332px;font-size:16.5px;font-weight:300">Your website readable on all devices</div>
<div class="abs hero-btn">MORE INFORMATION
  <svg width="10" height="10" viewBox="0 0 10 10"><circle cx="5" cy="5" r="5" fill="currentColor"/><path d="M4 2.8 6.2 5 4 7.2" stroke="#fff" stroke-width="1.4" fill="none"/></svg>
</div>
<div class="abs slide-arrow" style="left:28px"><svg width="26" height="26"><path d="M15 8 10 13l5 5" stroke="#fff" stroke-width="1.8" fill="none"/></svg></div>
<div class="abs slide-arrow" style="left:843px"><svg width="26" height="26"><path d="M11 8l5 5-5 5" stroke="#fff" stroke-width="1.8" fill="none"/></svg></div>

<h2 class="abs section-title" style="left:74px">BLOG ITEMS</h2>
<h2 class="abs section-title" style="left:624px">TESTIMONIALS</h2>

<article class="abs blog-card" style="left:74px;top:552px;background:linear-gradient(160deg,#6d7c78,#3d4a55)" role="img" aria-label="Photo of a team working together at a laptop">
  <div class="abs blog-date"><span class="ico"><svg width="9" height="9"><circle cx="4.5" cy="4.5" r="3.6" stroke="#fff" fill="none"/><path d="M4.5 2.5v2h1.5" stroke="#fff" fill="none"/></svg></span><span class="lbl">19.00 PM - JULY 12</span></div>
  <div class="abs blog-caption">Nemo Enim Ipsam Voluptatem</div>
</article>
<article class="abs blog-card" style="left:337px;top:552px;background:linear-gradient(160deg,#6b5a48,#2f2a26)" role="img" aria-label="Photo of a desk with a laptop showing web design">
  <div class="abs blog-date"><span class="ico"><svg width="9" height="9"><circle cx="4.5" cy="4.5" r="3.6" stroke="#fff" fill="none"/><path d="M4.5 2.5v2h1.5" stroke="#fff" fill="none"/></svg></span><span class="lbl">19.00 PM - JULY 12</span></div>
  <div class="abs blog-caption">Nemo Enim Ipsam Voluptatem</div>
</article>
<article class="abs blog-card" style="left:74px;top:751px;background:linear-gradient(180deg,#7c7f82,#3c3f44)" role="img" aria-label="Photo of a man working on a laptop outdoors">
  <div class="abs blog-date"><span class="ico"><svg width="9" height="9"><circle cx="4.5" cy="4.5" r="3.6" stroke="#fff" fill="none"/><path d="M4.5 2.5v2h1.5" stroke="#fff" fill="none"/></svg></span><span class="lbl">19.00 PM - JULY 12</span></div>
  <div class="abs blog-caption">Nemo Enim Ipsam Voluptatem</div>
</article>
<article class="abs blog-card" style="left:337px;top:751px;background:linear-gradient(160deg,#7a6c5c,#3a332c)" role="img" aria-label="Photo of a woman lying next to a laptop and breakfast">
  <div class="abs blog-date"><span class="ico"><svg width="9" height="9"><circle cx="4.5" cy="4.5" r="3.6" stroke="#fff" fill="none"/><path d="M4.5 2.5v2h1.5" stroke="#fff" fill="none"/></svg></span><span class="lbl">19.00 PM - JULY 12</span></div>
  <div class="abs blog-caption">Nemo Enim Ipsam Voluptatem</div>
</article>

<blockquote class="abs quote" style="top:562px"><span class="quote-mark">“</span>Lorem ipsum dolor sit amet, consectetur adipiscing elit, sed do eiusmod tempor incididunt ut labore et dolore magna aliqua. Ut enim ad minim veniam, quis nostrud exercitation Lorem ipsum dolor sit amet,</blockquote>
<div class="abs avatar" style="left:630px;top:675px;background:linear-gradient(180deg,#c9d2da,#4a5563)" role="img" aria-label="Portrait photo of a man in a suit"></div>
<div class="abs person" style="top:680px"><span class="name">John Doe -</span> Manager</div>
<div class="abs pager" style="top:711px"><span>‹</span><span>›</span></div>

<blockquote class="abs quote" style="top:761px"><span class="quote-mark">“</span>Lorem ipsum dolor sit amet, consectetur adipiscing elit, sed do eiusmod tempor incididunt ut labore et dolore magna aliqua. Ut enim ad minim veniam, quis nostrud exercitation Lorem ipsum dolor sit amet,</blockquote>
<div class="abs avatar" style="left:630px;top:874px;background:linear-gradient(180deg,#e7d3c3,#c9a889)" role="img" aria-label="Portrait photo of a woman"></div>
<div class="abs person" style="top:879px"><span class="name">John Doe -</span> Manager</div>
<div class="abs pager" style="top:910px"><span>‹</span><span>›</span></div>

<footer class="abs site-footer"></footer>
<h3 class="abs footer-title" style="left:73px">ABOUT OUR COMPANY</h3>
<p class="abs footer-text" style="left:73px;top:1035px;width:285px">rem ipsum dolor sit amet, consectetur adipisicing elit. Minima, minus iure accusantium dolores, officiis eveniet architecto error placeat ratione incidunt? rem ipsum dolor sit amet, consectetur adipisicing elit. Minima, minus iure accusantium dolores,</p>
<span class="abs social" style="left:73px;background:#dd4b39"></span>
<span class="abs social" style="left:101px;background:#3b5998"></span>
<span class="abs social" style="left:129px;background:#1da1f2"></span>
<span class="abs social" style="left:157px;background:#0e76a8"></span>
<span class="abs social" style="left:185px;background:#e52d27"></span>

<h3 class="abs footer-title" style="left:421px">SIGN UP FOR NEWSLETTER</h3>
<p class="abs footer-text" style="left:421px;top:1035px;width:200px;text-align:justify">Excepteur sint occaecat cupidatat non proident, sunt in culpa qui officia deserunt</p>
<div class="abs news-input">Enter Name</div>
<div class="abs news-btn">SUBSCRIBE</div>

<h3 class="abs footer-title" style="left:696px">CONTACT US</h3>
<p class="abs footer-text" style="left:696px;top:1033px;font-size:9.8px;color:#333">Birchline<br>PO BOX TBA, Millbrook</p>
<div class="abs contact-line" style="top:1074px">
  <svg width="14" height="14" viewBox="0 0 14 14"><path d="M3 1.5 5 4 4 5.5c.8 1.8 2.2 3.2 4 4L9.5 8.5 12 10.5 11 12.5C6 12 2 8 1.5 3Z" stroke="var(--green)" fill="none"/></svg>+1 5550 123 456</div>
<div class="abs contact-line" style="top:1093px">
  <svg width="14" height="14" viewBox="0 0 14 14"><rect x="1" y="3" width="12" height="8" stroke="var(--green)" fill="none"/><path d="M1 3l6 5 6-5" stroke="var(--green)" fill="none"/></svg>info@birchline-studio.com</div>

<div class="abs bottom-bar">©2014 - 2015 &nbsp;<b>BIRCHLINE.</b>, All Rights Reserved.</div>

</body>
</html>
```